Private Dining Restaurant Menu Design

Looking for help in designing a private dining room menu brochure - probably would need 4 panel layout to make all of the content fit, or a 5.5x8" booklet. Open to your ideas on layout/vessel - would want to post on website and be able to print to hand out to guests interested in booking our private dining room.

All content is in the attached "Private Dining Menu".

Would like to match existing dinner menu design - also attached.

Website is www.tallowfenkitchen.com

Requirements
Must have
• Easy to read format of a brochure of the private dining menu content - want to be able to hand out to interested guests and have it simple and easy to read/flip through.

```html
<!DOCTYPE html>
<html lang="en">
<head>
<meta charset="utf-8">
<title>Lunch Options – Tallowfen Kitchen</title>
<link rel="stylesheet" href="https://fonts.googleapis.com/css2?family=Arimo:wght@400;700&family=Tinos:wght@700&display=swap">
<style>
  :root {
    --navy: #1f2b5c;
    --cream: #fbf8e1;
    --ink: #141414;
    --ghost: #ece4c4;
    --ghost-soft: #f1ead0;
  }
  * { margin: 0; padding: 0; box-sizing: border-box; }
  html, body { width: 1200px; height: 825px; overflow: hidden; }
  body { background: var(--navy); font-family: "Arimo", Arial, sans-serif; color: var(--ink); }
  .menu-card {
    position: absolute; left: 25px; top: 21px; width: 1150px; height: 783px;
    background: var(--cream); overflow: hidden;
  }
  .backdrop-scene {
    position: absolute; left: 330px; top: 70px; width: 520px; height: 240px;
    background: radial-gradient(ellipse at 50% 60%, var(--ghost-soft) 0%, rgba(241,234,208,0) 70%);
  }
  .backdrop-name {
    position: absolute; left: 0; right: 0; top: 380px;
    text-align: right; padding-right: 0;
    font-weight: 700; font-size: 170px; letter-spacing: 4px; line-height: 1;
    color: var(--ghost); white-space: nowrap;
  }
  .backdrop-tag {
    position: absolute; left: 0; right: 0; top: 655px; text-align: center;
    font-weight: 700; font-size: 62px; letter-spacing: 6px; color: var(--ghost);
  }
  .title-rule { position: absolute; top: 48px; height: 2px; background: var(--ink); }
  .title-rule.left { left: 75px; width: 244px; }
  .title-rule.right { left: 850px; width: 208px; }
  .menu-title {
    position: absolute; left: 0; right: 0; top: 31px; text-align: center;
    font-family: "Tinos", "Times New Roman", serif; font-weight: 700; font-size: 23px; letter-spacing: .5px;
  }
  .menu-note { position: absolute; left: 0; right: 0; top: 60px; text-align: center; font-size: 15.5px; }
  .option { position: absolute; left: 21px; right: 20px; font-size: 15.5px; line-height: 21px; }
  .option h2 { font-size: 15.5px; font-weight: 700; }
  .option ul { list-style: none; margin-left: 104px; }
  .option li { padding-left: 10px; text-indent: -10px; }
  .option li::before { content: "- "; }
  .option-a { top: 144px; }
  .option-b { top: 310px; }
  .option-c { top: 487px; }
</style>
</head>
<body>
<main class="menu-card">
  <div class="backdrop-scene" role="img" aria-label="Faint mountain and pine tree scene in the background"></div>
  <div class="backdrop-name" aria-hidden="true">TALLOWFEN</div>
  <div class="backdrop-tag" aria-hidden="true">TALLOWFEN KITCHEN</div>

  <span class="title-rule left"></span>
  <span class="title-rule right"></span>
  <h1 class="menu-title">LUNCH OPTIONS</h1>
  <p class="menu-note">(an option must be chosen for groups of 15 or more, served before 3pm)</p>

  <section class="option option-a">
    <h2>Option A - $10.00-$12.00 / Person.</h2>
    <p>Pick Two Lunch Menu – Soup / Salad ($10.00), Soup/Sandwich ($11.00), or Salad / Sandwich ($12.00).</p>
    <ul>
      <li>Sandwiches: ½ Turkey Club, ½ BLTA, BBQ Pork Sliders (2), Wood-Roasted Rotisserie Chicken Sliders (2),<br>Walleye Tacos (2), or Chicken Tacos (2).</li>
      <li>Soups: Chicken Wild Rice, White Chicken Chili, or Soup of the Day.</li>
      <li>Salads: Wedge, House, or Caesar Salad.</li>
    </ul>
  </section>

  <section class="option option-b">
    <h2>Option B - $13.00 / Person.</h2>
    <p>Served with your choice of fries, cheesy hashbrowns, soup, or apple cabbage slaw.</p>
    <ul>
      <li>Applewood Bacon &amp; Fajita Chicken Salad.</li>
      <li>Rotisserie Chicken Salad.</li>
      <li>Brown Sugar Bacon and Smoked Cheddar Burger.</li>
      <li>Pepperjack Turkey Melt.</li>
      <li>Walleye Fish Tacos.</li>
    </ul>
  </section>

  <section class="option option-c">
    <h2>Option C - $13.00 / Person Buffet Option.</h2>
    <p>Food ready upon arrival, or at a set time of your choice.</p>
    <ul>
      <li>Sandwich platter – Assorted Rotisserie Turkey Club, Ham and Cheese, and Veggie Wrap.</li>
      <li>Rotisserie Chicken Salad Bar.</li>
      <li>Fresh Fruit Platter.</li>
      <li>House-made Potato Chips.</li>
    </ul>
  </section>
</main>
</body>
</html>
```